Business Card Design

The new Company is called The Harbor Pantry - based in Miami Beach, Florida and Connecticut. We want a business card to be catchy and memorable ( like our Company name). Our business is marketing and retail sales of flavored cashew nuts in boutique /high end stores. The new business card must include a logo which must be a cashew nut with a king's crown or Roman wreath.
Yes- we are looking for a logo to be designed for the business and for the business card.

Industry/Entity Type

Marketing

Font styles to use
Script

```html
<!DOCTYPE html>
<html lang="en">
<head>
<meta charset="utf-8">
<title>The Harbor Pantry — Business Card</title>
<link rel="stylesheet" href="https://fonts.googleapis.com/css2?family=Orbitron:wght@500;700&display=swap">
<style>
  :root {
    --stage: #141414;
    --paper: #ffffff;
    --amber: #e0953c;
    --amber-deep: #c9792a;
    --copper: #b8774f;
    --copper-light: #cf9872;
    --nut-light: #f4e8d8;
    --nut-mid: #e6cfae;
    --nut-warm: #d9b68a;
    --nut-shadow: #c29a6e;
  }
  * { margin: 0; padding: 0; box-sizing: border-box; }
  html, body { width: 1200px; height: 974px; overflow: hidden; }
  body {
    position: relative;
    background: var(--stage);
    font-family: "Orbitron", "Arial Narrow", sans-serif;
    font-variant: small-caps;
  }

  .card {
    position: absolute;
    top: 190px;
    width: 540px;
    height: 310px;
    overflow: hidden;
    border-radius: 2px;
    box-shadow: 0 8px 22px rgba(0,0,0,0.6);
  }
  .nut-photo { position: absolute; inset: 0; }
  .brand-dot { flex: none; border-radius: 50%; background: var(--amber); }

  /* Front: contact side */
  .card--front { left: 40px; background: var(--paper); }
  .card--front .nut-photo {
    background:
      linear-gradient(180deg, rgba(255,255,255,0) 0%, rgba(255,255,255,0.35) 40%, rgba(255,255,255,0.9) 62%, var(--paper) 75%),
      linear-gradient(90deg, var(--paper) 0%, rgba(255,255,255,0.6) 18%, rgba(255,255,255,0) 40%),
      radial-gradient(ellipse 22% 30% at 30% 18%, var(--nut-warm), rgba(217,182,138,0) 100%),
      radial-gradient(ellipse 20% 28% at 55% 12%, var(--nut-shadow), rgba(194,154,110,0) 100%),
      radial-gradient(ellipse 24% 32% at 78% 22%, var(--nut-warm), rgba(217,182,138,0) 100%),
      radial-gradient(ellipse 18% 26% at 92% 8%, var(--nut-shadow), rgba(194,154,110,0) 100%),
      linear-gradient(180deg, var(--nut-mid), var(--nut-light));
  }
  .card--front .brand {
    position: absolute; left: 30px; bottom: 36px;
    display: flex; flex-direction: column; align-items: flex-start; gap: 10px;
    color: var(--amber); font-size: 14px; font-weight: 500; letter-spacing: 0.5px;
  }
  .card--front .brand-dot { width: 42px; height: 42px; margin-left: 30px; }
  .card--front .person {
    position: absolute; right: 34px; bottom: 26px;
    display: flex; flex-direction: column; align-items: flex-start;
    color: var(--amber-deep);
  }
  .person-details {
    list-style: none; margin-bottom: 8px;
    font-size: 12px; font-weight: 700; line-height: 1.4; letter-spacing: 1px;
  }
  .person-name { font-size: 34px; font-weight: 700; letter-spacing: 2px; line-height: 1; }

  /* Back: brand side */
  .card--back { left: 620px; background: var(--copper); }
  .card--back .nut-photo {
    background:
      radial-gradient(ellipse 16% 22% at 35% 30%, var(--nut-warm), rgba(217,182,138,0) 100%),
      radial-gradient(ellipse 16% 22% at 62% 65%, var(--nut-shadow), rgba(194,154,110,0) 100%),
      radial-gradient(ellipse 18% 24% at 72% 25%, var(--nut-warm), rgba(217,182,138,0) 100%),
      radial-gradient(ellipse 60% 85% at 50% 50%, var(--nut-light) 0%, var(--nut-mid) 45%, rgba(184,119,79,0) 100%),
      linear-gradient(135deg, var(--copper-light), var(--copper));
  }
  .card--back .brand {
    position: absolute; inset: 0;
    display: flex; flex-direction: column; align-items: center; justify-content: center; gap: 18px;
    color: var(--amber); font-size: 32px; font-weight: 700; letter-spacing: 1.5px;
  }
  .card--back .brand-dot { width: 86px; height: 86px; }

  /* Brand strip */
  .strip {
    position: absolute; left: 0; top: 790px;
    width: 1200px; height: 184px;
  }
  .strip .nut-photo {
    background:
      linear-gradient(90deg, var(--paper) 0%, var(--paper) 27%, rgba(255,255,255,0) 48%),
      radial-gradient(ellipse 9% 45% at 42% 55%, var(--nut-warm), rgba(217,182,138,0) 100%),
      radial-gradient(ellipse 10% 50% at 62% 50%, var(--nut-warm), rgba(217,182,138,0) 100%),
      radial-gradient(ellipse 9% 45% at 80% 58%, var(--nut-shadow), rgba(194,154,110,0) 100%),
      radial-gradient(ellipse 8% 40% at 95% 45%, var(--nut-warm), rgba(217,182,138,0) 100%),
      linear-gradient(180deg, var(--nut-light), var(--nut-mid));
  }
  .strip .brand {
    position: absolute; left: 42px; bottom: 14px;
    display: flex; flex-direction: column; align-items: center; gap: 16px;
    color: var(--amber); font-size: 24px; font-weight: 500; letter-spacing: 1.5px;
  }
  .strip .brand-dot { width: 96px; height: 96px; }
</style>
</head>
<body>
  <section class="card card--front">
    <div class="nut-photo" role="img" aria-label="Close-up photograph of roasted cashew nuts fading into white"></div>
    <div class="brand"><span class="brand-dot"></span><span>The Harbor Pantry</span></div>
    <div class="person">
      <ul class="person-details">
        <li>Contact</li>
        <li>Address</li>
        <li>E-mail</li>
      </ul>
      <h1 class="person-name">Your Name</h1>
    </div>
  </section>

  <section class="card card--back">
    <div class="nut-photo" role="img" aria-label="Photograph of a heap of roasted cashew nuts on a copper background"></div>
    <div class="brand"><span class="brand-dot"></span><span>The Harbor Pantry</span></div>
  </section>

  <section class="strip">
    <div class="nut-photo" role="img" aria-label="Close-up photograph of cashew nuts fading into white on the left"></div>
    <div class="brand"><span class="brand-dot"></span><span>The Harbor Pantry</span></div>
  </section>
</body>
</html>
```